PREMIUM AGENCY High End Business Card - A+++ Designers Wanted

** DO NOT ATTEMPT TO CONTACT ME THROUGH SEARCHING ON ZINTREL OR EMAILING ME THROUGH MY WEBSITE **

I need a fresh, contemporary business card designed using the logo attached (BRONSALK)

I have attached the font for BRONSALK

It must have a premium look and feel. The business card size must be STANDARD size.

You can submit either/both VERTICAL or HORIZONTAL designs.

FRONT: It must have the following sample information on

Paul Ardley
Director Operations
Mobile +61 452 118 906
Email paulardley@bronsalk.com
www.bronsalk.com

The REAR of the business card must have the words

DESIGN ELEVATE FUTURE

as part of the design, in the same font (NEXA) attached.

The words do not need to be in capitals, or on the same line, please design this as you see it best working.

ADDITIONAL INFORMATION
======================

The BRONSALK logo must be on the front of the card

I want Ultraviolet printing on the final design, to enhance either the NAME of the person OR the BRONSALK logo OR the words on the back of the card.

Target Market(s)

Agency, Advertising Agency, Creative, Designers

Industry/Entity Type

Media

Contact Information for Business Card

Design Agency, Contemporary, Premium look and feel, High Quality

Font styles to use
Serif
Sans Serif
Other font styles liked:
• ATTACHED TO PROJECT

Requirements
Must have
• BLACK & WHITE as the primary design, and if you feel there can be a highlighted colour, then this can be used.
• The Logo ICON attached is blue, this colour must not be changed.
• I have attached the partner brand BRONSALK MEDIA incase you need to manipulate the original files.
• ** DO NOT ATTEMPT TO CONTACT ME THROUGH SEARCHING ON ZINTREL OR EMAILING ME THROUGH MY WEBSITE **
Nice to have
• Must be Premium. I have attached some sample designs, that I like that would be a good inspiration for where this can be taken.
• My favourite design is is the KESTRAVUE2-BUSINESSCARD-TEMPLATE
Should not have
• No funny or silly standard / off the shelf designs

```html
<!DOCTYPE html>
<html lang="en">
<head>
<meta charset="utf-8">
<title>Bronsalk Business Card</title>
<link href="https://fonts.googleapis.com/css2?family=Montserrat:wght@300;400;600;700&display=swap" rel="stylesheet">
<style>
  :root {
    --stage: #2a2a2a;
    --card-white: #f7f7f7;
    --card-black: #171717;
    --ink: #222222;
    --ink-soft: #555555;
    --brand-blue: #3a9ad9;
    --uv-ink: #3d3d3d;
    --uv-soft: #4a4a4a;
  }
  * { margin: 0; padding: 0; box-sizing: border-box; }
  html, body {
    width: 1200px; height: 873px; overflow: hidden;
    background: var(--stage);
    font-family: "Montserrat", sans-serif;
  }
  .canvas {
    position: relative; width: 1200px; height: 873px;
    display: flex; align-items: center; justify-content: center; gap: 40px;
  }
  .card {
    position: relative; width: 540px; height: 316px; overflow: hidden;
    box-shadow: 0 14px 30px rgba(0,0,0,.45);
  }
  /* Front */
  .card-front { background: var(--card-white); }
  .brand-row {
    position: absolute; left: 46px; top: 70px;
    display: flex; align-items: center; gap: 18px;
  }
  .brand-mark {
    width: 30px; height: 30px; border-radius: 50%;
    background: var(--brand-blue);
  }
  .brand-name {
    font-weight: 700; font-size: 44px; letter-spacing: 5px; color: var(--ink);
  }
  .person {
    position: absolute; right: 290px; top: 196px; text-align: right;
  }
  .person-name {
    font-weight: 600; font-size: 17px; color: var(--brand-blue);
  }
  .person-role {
    font-weight: 400; font-size: 12px; color: var(--ink-soft); margin-top: 3px;
  }
  .divider {
    position: absolute; left: 268px; top: 160px; width: 2px; height: 92px;
    background: linear-gradient(to bottom, rgba(58,154,217,0), var(--brand-blue), rgba(58,154,217,0));
  }
  .contact-list {
    position: absolute; left: 290px; top: 164px; list-style: none;
  }
  .contact-item {
    display: flex; align-items: center; gap: 9px;
    font-size: 11.5px; color: var(--ink-soft); line-height: 24px;
  }
  .contact-icon { width: 13px; height: 13px; flex: none; }
  .accent-band { position: absolute; left: 0; bottom: 0; }
  /* Back */
  .card-back { background: var(--card-black); }
  .back-brand-row {
    position: absolute; left: 40px; top: 104px;
    display: flex; align-items: center; gap: 16px;
  }
  .back-mark {
    width: 26px; height: 26px; border-radius: 50%; background: var(--uv-ink);
  }
  .back-brand {
    font-weight: 600; font-size: 34px; letter-spacing: 3px; color: var(--uv-ink);
    white-space: nowrap;
  }
  .back-tagline {
    position: absolute; left: 82px; top: 210px;
    font-weight: 700; font-size: 17px; letter-spacing: 5px; color: var(--uv-soft);
    white-space: nowrap;
  }
</style>
</head>
<body>
<main class="canvas">
  <section class="card card-front">
    <div class="brand-row">
      <span class="brand-mark"></span>
      <span class="brand-name">BRONSALK</span>
    </div>
    <div class="person">
      <p class="person-name">Paul Ardley</p>
      <p class="person-role">Director Operations</p>
    </div>
    <div class="divider"></div>
    <ul class="contact-list">
      <li class="contact-item">
        <svg class="contact-icon" viewBox="0 0 16 16"><path fill="#3a9ad9" d="M3 2h3l1.5 3.5-2 1.2a8 8 0 0 0 3.8 3.8l1.2-2L14 10v3a1 1 0 0 1-1 1A11 11 0 0 1 2 3a1 1 0 0 1 1-1z"/></svg>
        +61 452 118 906
      </li>
      <li class="contact-item">
        <svg class="contact-icon" viewBox="0 0 16 16"><rect x="1" y="3" width="14" height="10" rx="1" fill="#3a9ad9"/><path d="M1.5 4 8 9l6.5-5" stroke="#fff" stroke-width="1.3" fill="none"/></svg>
        paulardley@bronsalk.com
      </li>
      <li class="contact-item">
        <svg class="contact-icon" viewBox="0 0 16 16"><g fill="none" stroke="#3a9ad9" stroke-width="1.8" stroke-linecap="round"><path d="M6.5 9.5 9.5 6.5"/><path d="M7 4.5 8.5 3a2.5 2.5 0 0 1 3.5 3.5L10.5 8"/><path d="M9 11.5 7.5 13A2.5 2.5 0 0 1 4 9.5L5.5 8"/></g></svg>
        www.bronsalk.com
      </li>
    </ul>
    <svg class="accent-band" width="540" height="316" viewBox="0 0 540 316">
      <path d="M330 316 Q332 286 362 284 L540 284 L540 316 Z" fill="#3a9ad9"/>
      <path d="M336 316 Q340 292 366 290 L540 290" stroke="#ffffff" stroke-width="1.5" fill="none" opacity=".55"/>
    </svg>
  </section>

  <section class="card card-back">
    <div class="back-brand-row">
      <span class="back-mark"></span>
      <span class="back-brand">BRONSALK MEDIA</span>
    </div>
    <p class="back-tagline">DESIGN ELEVATE FUTURE</p>
  </section>
</main>
</body>
</html>
```